Zielgruppe
Wir sind ein junges Unternehmen im Bereich der Werbemittelbranche. Wir vertreiben u.a. Seccodosen im individuellen Design nach Kundenwunsch nur an B2B. Wir möchten eine Secco Dose entwickeln lassen, die
- als Eigenwerbung dienen soll (Abgabe an potentielle B2B Kunden ) und
- als Secco im Handel (Kioske, Touristshops B2C )
genutzt / verkauft werden kann.
Dies vor dem Hintergrund von möglichen sportlichen Großereignissen in Köln
(weitere Zielgruppenspezifische Ideen in Planung)
Aufgabenstellung
Entwicklung eines Dosenetiketts (PE-Kunststoffetikett) für eine 200 ML Secco Dose. Inhalt orginal italienischer IGT Secco Bianco.
Pflichttexte und Druckvorgaben/Stanze für Etikett wird geliefert.
Name: RheinPerlwein
Markantes plakatives Design.
Ggf. Nutzung der Kölner Signalfarben rot - schwarz- weiss
Hinweis zur Gestaltung - Optik.
Dosenmaterial Aluminium.
Es gibt 2 Optionen, die für die Gestaltung /Optik interessant sind:
1. Druck auf transparenter Folie. Optischer Eindruck wie ein Direktdruck auf Dose.
2. 1-4 C Druck auf weißer Folie

```html
<!DOCTYPE html>
<html lang="de">
<head>
<meta charset="utf-8">
<title>RheinPerlwein – Dosenetikett</title>
<link rel="stylesheet" href="https://fonts.googleapis.com/css2?family=Roboto+Slab:wght@400;700;800&display=swap">
<style>
  :root {
    --paper: #ffffff;
    --label-black: #0a0a0a;
    --type-white: #ffffff;
    --koeln-red: #e3101a;
  }
  html, body {
    margin: 0;
    padding: 0;
    width: 945px;
    height: 1200px;
    overflow: hidden;
    background: var(--paper);
  }
  .label {
    display: block;
    width: 945px;
    height: 1200px;
  }
  .label-ground { fill: var(--label-black); }
  .saying {
    font-family: "Roboto Slab", serif;
    fill: var(--type-white);
    text-anchor: middle;
  }
  .saying--light { font-weight: 400; }
  .saying--bold { font-weight: 800; }
  .saying--red { fill: var(--koeln-red); font-weight: 800; }
  .product-name {
    font-family: "Roboto Slab", serif;
    font-weight: 800;
    fill: var(--type-white);
    text-anchor: middle;
  }
  .name-dot { fill: var(--koeln-red); }
</style>
</head>
<body>
<svg class="label" viewBox="0 0 945 1200" xmlns="http://www.w3.org/2000/svg" aria-label="Dosenetikett RheinPerlwein">
  <rect class="label-ground" x="150" y="50" width="645" height="1100"/>

  <g class="sayings sayings--top">
    <text class="saying saying--light" x="472.5" y="175" font-size="66" textLength="570" lengthAdjust="spacingAndGlyphs">ET ES WIE ET ES.</text>
    <text class="saying saying--light" x="472.5" y="240" font-size="54" textLength="570" lengthAdjust="spacingAndGlyphs">ET KÜTT WIE ET KÜTT.</text>
    <text class="saying saying--bold" x="472.5" y="285" font-size="34" textLength="570" lengthAdjust="spacingAndGlyphs">ET HÄTT NOCH IMMER JOT JEJANGE.</text>
    <text class="saying saying--bold" x="472.5" y="350" font-size="52" textLength="570" lengthAdjust="spacingAndGlyphs">WAT FOTT ES ES FOTT.</text>
    <text class="saying saying--bold" x="472.5" y="410" font-size="46" textLength="560" lengthAdjust="spacingAndGlyphs">NIX BLIEV WIE ET WOR.</text>
  </g>

  <g class="product">
    <text class="product-name" x="472.5" y="660" font-size="88" textLength="560" lengthAdjust="spacingAndGlyphs">RheinPerlwein</text>
    <rect class="name-dot" x="742" y="572" width="16" height="16"/>
  </g>

  <g class="sayings sayings--bottom">
    <text class="saying saying--bold" x="472.5" y="830" font-size="24" textLength="570" lengthAdjust="spacingAndGlyphs">KENNE MER NIT, BRUCHE MER NIT, FOTT DOMET.</text>
    <text class="saying saying--bold" x="472.5" y="895" font-size="52" textLength="570" lengthAdjust="spacingAndGlyphs">WAT WELLSTE MAACHE?</text>
    <text class="saying saying--bold" x="472.5" y="950" font-size="38" textLength="570" lengthAdjust="spacingAndGlyphs">MACH ET JOT ÄVVER NIT ZE OFF.</text>
    <text class="saying saying--bold" x="472.5" y="1012" font-size="50" textLength="570" lengthAdjust="spacingAndGlyphs">WAT SOLL DÄ QUATSCH?</text>
    <text class="saying saying--red" x="472.5" y="1080" font-size="52" textLength="570" lengthAdjust="spacingAndGlyphs">DRINKSTE ENE MET?</text>
  </g>
</svg>
</body>
</html>
```